metal roofing website

I have several domain names and a website that has been built. I need someone to recreate essentially the same website and change some photos and basic design to create the new sites. I have all of the files and c panel access to the lucky winner. If you can do a good job at a fair price I will have 100's of sites to send to you very soon. I have the site built and have all files just need it recreated on my server. the current site is www.dorvanemetalinc.com I am looking to get this done ASAP!!!

```html
<!DOCTYPE html>
<html lang="en">
<head>
<meta charset="utf-8">
<title>Dorvane Metal Inc.</title>
<link href="https://fonts.googleapis.com/css2?family=Roboto:wght@400;500;700&family=Open+Sans:wght@400;600&display=swap" rel="stylesheet">
<style>
:root{
  --red:#e21b23;
  --dark:#111;
  --text:#555;
  --muted:#888;
  --light:#f2f2f2;
  --border:#d9d9d9;
  --white:#fff;
}
*{box-sizing:border-box;margin:0;padding:0}
html,body{width:1200px;height:3838px;overflow:hidden;background:var(--white)}
body{position:relative;font-family:'Open Sans',Arial,sans-serif;color:var(--text)}
.abs{position:absolute}
.heading{font-family:'Roboto',Arial,sans-serif;font-weight:700;color:var(--dark);text-transform:uppercase}
.rule{position:absolute;height:4px;background:var(--red)}
.pill{position:absolute;border:2px solid #ccc;border-radius:30px;display:flex;align-items:center;justify-content:center;font-family:'Roboto',Arial,sans-serif;font-weight:700;font-size:15px;color:var(--red);text-transform:uppercase;background:var(--white)}

/* header */
.site-header{position:absolute;left:0;top:0;width:1200px;height:120px;background:var(--white)}
.brand{position:absolute;left:112px;top:30px;display:flex;align-items:center;gap:12px;font-family:'Roboto',Arial,sans-serif;font-weight:700;font-size:26px;color:#8b1a1a;text-transform:uppercase}
.brand-mark{width:22px;height:22px;background:#8b1a1a}
.call{position:absolute;left:660px;top:27px;display:flex;align-items:center;gap:10px;font-family:'Roboto',Arial,sans-serif;font-weight:700;font-size:17px;color:var(--dark)}
.call span{color:var(--red)}
.nav{position:absolute;top:82px;left:0;font-family:'Roboto',Arial,sans-serif;font-weight:700;font-size:15px;color:var(--dark);text-transform:uppercase}
.nav a{position:absolute;white-space:nowrap;color:inherit;text-decoration:none}
.nav a.active{color:var(--red)}

/* hero */
.hero{position:absolute;left:0;top:120px;width:1200px;height:537px;background:linear-gradient(180deg,#6d7073 0%,#8a8c8c 45%,#6b665c 75%,#4e4637 100%)}
.hero-title{position:absolute;left:0;width:1200px;top:138px;text-align:center;font-family:'Roboto',Arial,sans-serif;font-weight:700;font-size:56px;line-height:76px;color:var(--white);text-transform:uppercase}
.hero-btn{position:absolute;left:486px;top:320px;width:228px;height:59px;border:2px solid var(--white);border-radius:30px;display:flex;align-items:center;justify-content:center;color:var(--white);font-family:'Roboto',Arial,sans-serif;font-weight:700;font-size:16px;text-transform:uppercase}
.dots{position:absolute;top:459px;left:566px;display:flex;gap:5px}
.dots i{width:13px;height:13px;border:2px solid var(--white);border-radius:50%}
.dots i.on{background:var(--white)}

/* welcome */
.welcome-title{left:112px;top:745px;font-size:37px;line-height:50px}
.welcome-text{left:112px;top:897px;width:460px;font-size:13px;line-height:29px;color:var(--text)}
.video{position:absolute;left:634px;top:755px;width:453px;height:314px;background:linear-gradient(135deg,#8a9aaa 0%,#4b5663 45%,#9aa0a6 100%)}
.play{position:absolute;left:196px;top:127px;width:62px;height:62px;border-radius:50%;background:var(--dark);display:flex;align-items:center;justify-content:center}

/* services */
.services{position:absolute;left:0;top:1218px;width:1200px;height:629px;background:var(--light)}
.section-title{position:absolute;left:0;width:1200px;text-align:center;font-size:37px}
.card{position:absolute;width:473px;height:141px;background:var(--white);border:1px solid #ddd;box-shadow:0 2px 6px rgba(0,0,0,.12)}
.card svg{position:absolute;left:22px;top:32px}
.card h3{position:absolute;left:120px;top:26px;font-family:'Roboto',Arial,sans-serif;font-weight:500;font-size:23px;color:var(--dark)}
.card p{position:absolute;left:120px;top:68px;width:320px;font-size:13px;line-height:26px;color:var(--text)}

/* gallery */
.photo{position:absolute}

/* contact */
.contact{position:absolute;left:0;top:3164px;width:1200px;height:674px;background:var(--light)}
.sub-title{position:absolute;font-family:'Roboto',Arial,sans-serif;font-weight:500;font-size:20px;color:var(--dark)}
.field{position:absolute;border:1px solid #999;background:var(--white);font-size:11px;color:var(--muted);padding:8px 12px}
.info{position:absolute;left:778px;font-size:15px;color:var(--text);line-height:28px}
.info-icon{position:absolute;left:778px;width:34px;height:34px;border:2px solid #ccc;border-radius:50%;background:var(--white);display:flex;align-items:center;justify-content:center}
.footer-rule{position:absolute;left:112px;top:3730px;width:968px;height:1px;background:var(--border)}
.copyright{position:absolute;left:112px;top:3768px;font-size:13px;color:var(--text)}
.social{position:absolute;top:3760px;width:36px;height:36px;border:2px solid #ccc;border-radius:50%;background:var(--white);display:flex;align-items:center;justify-content:center}
.social i{width:12px;height:12px;background:var(--red);border-radius:50%}
</style>
</head>
<body>

<header class="site-header">
  <div class="brand"><span class="brand-mark"></span>Dorvane Metal</div>
  <div class="call">
    <svg width="16" height="16" viewBox="0 0 24 24"><path fill="#e21b23" d="M6.6 10.8a15 15 0 0 0 6.6 6.6l2.2-2.2a1 1 0 0 1 1-.25 11.4 11.4 0 0 0 3.6.57 1 1 0 0 1 1 1V20a1 1 0 0 1-1 1A17 17 0 0 1 3 4a1 1 0 0 1 1-1h3.5a1 1 0 0 1 1 1c0 1.25.2 2.45.57 3.57a1 1 0 0 1-.25 1z"/></svg>
    CALL NOW: <span>555-012-0765</span>
  </div>
  <div class="pill" style="left:939px;top:13px;width:148px;height:49px">Visualizer</div>
  <nav class="nav">
    <a class="active" style="left:524px">Home</a>
    <a style="left:606px">About Us</a>
    <a style="left:721px">Services</a>
    <a style="left:831px">Gallery</a>
    <a style="left:939px">Contact Us</a>
    <svg class="abs" style="left:1073px;top:1px" width="16" height="16" viewBox="0 0 24 24"><circle cx="10" cy="10" r="7" fill="none" stroke="#111" stroke-width="3"/><path d="M15 15l6 6" stroke="#111" stroke-width="3"/></svg>
  </nav>
</header>

<section class="hero" role="img" aria-label="Large metal post frame building with garage doors under a cloudy sky">
  <h1 class="hero-title">Manufacturers of Quality<br>Building Components</h1>
  <div class="hero-btn">Get More Info</div>
  <div class="dots"><i class="on"></i><i></i><i></i><i></i></div>
</section>

<section class="welcome">
  <h2 class="heading abs welcome-title">Welcome to<br>Dorvane Metal</h2>
  <div class="rule" style="left:112px;top:860px;width:151px"></div>
  <p class="abs welcome-text">Nam libero tempore, cum soluta nobis est eligendi optio cumque nihil impedit quo minus id quod maxime placeat facere possimus, omnis vo luptas assumenda est, omnis dolor repellendus. Temporibus autem qu ibusdam et aut officiis debitis aut rerum necessitatibus saepe eveniet et voluptates repudiandae sint et mole.</p>
  <div class="pill" style="left:112px;top:1074px;width:154px;height:52px">Read More</div>
  <div class="video" role="img" aria-label="Worker cutting a metal roofing panel">
    <div class="play"><svg width="24" height="24" viewBox="0 0 24 24"><path d="M7 4l13 8-13 8z" fill="#fff"/></svg></div>
  </div>
</section>

<section class="services">
  <h2 class="heading section-title" style="top:92px">Our Services</h2>
  <div class="rule" style="left:524px;top:161px;width:152px"></div>

  <div class="card" style="left:112px;top:227px">
    <svg width="64" height="64" viewBox="0 0 64 64" fill="none" stroke="#e21b23" stroke-width="3"><path d="M12 26L32 12l20 14"/><rect x="14" y="26" width="36" height="26"/><rect x="24" y="36" width="16" height="16"/><path d="M6 56h52M28 4h8v8h-8z"/></svg>
    <h3>Complete Post frame building</h3>
    <p>Call us for a quote, or stop in and we can help you design</p>
  </div>
  <div class="card" style="left:614px;top:227px">
    <svg width="64" height="64" viewBox="0 0 64 64" fill="none" stroke="#e21b23" stroke-width="3"><path d="M6 32L32 10l26 22"/><path d="M14 26v28h36V26"/><rect x="27" y="36" width="10" height="18"/></svg>
    <h3>Residential Metal Roofing</h3>
    <p>Super rib, snap-loc and a variety of metal roofing options</p>
  </div>
  <div class="card" style="left:112px;top:401px">
    <svg width="64" height="64" viewBox="0 0 64 64" fill="none" stroke="#e21b23" stroke-width="3"><path d="M8 10h48v44H8z"/><path d="M16 10v44M24 10v44M32 10v44M40 10v44M48 10v44"/></svg>
    <h3>Prefab Sheets</h3>
    <p>Call us for a quote, or stop in and we can help you design</p>
  </div>
  <div class="card" style="left:614px;top:401px">
    <svg width="64" height="64" viewBox="0 0 64 64" fill="none" stroke="#e21b23" stroke-width="3"><path d="M6 24l14-12h24l14 12"/><rect x="10" y="24" width="44" height="30"/><path d="M18 34h28v20H18zM18 34l28 20M46 34L18 54"/></svg>
    <h3>Agricultural &amp; Commercial</h3>
    <p>28 gauge panels are the thickest and strongest in the industry.</p>
  </div>
</section>

<section class="gallery">
  <h2 class="heading section-title" style="top:1928px">Our Gallery</h2>
  <div class="rule" style="left:524px;top:1993px;width:152px"></div>
  <div class="photo" role="img" aria-label="Dark barn with silo" style="left:0;top:2075px;width:391px;height:273px;background:linear-gradient(180deg,#b7c7d8,#2b2a2c 60%,#3b3a30)"></div>
  <div class="photo" role="img" aria-label="Country house with porch on green lawn" style="left:404px;top:2075px;width:392px;height:273px;background:linear-gradient(180deg,#c9d2d9,#9b9a86 55%,#3f6a25)"></div>
  <div class="photo" role="img" aria-label="Green metal roof seen from above" style="left:808px;top:2075px;width:392px;height:273px;background:linear-gradient(135deg,#4f6a3a,#2f7f6e 50%,#7a3a28)"></div>
  <div class="photo" role="img" aria-label="Elevated cabin with staircase in snow" style="left:0;top:2361px;width:391px;height:560px;background:linear-gradient(180deg,#5c8fd0,#8aa6c4 40%,#6e5a44 65%,#e8ecf0)"></div>
  <div class="photo" role="img" aria-label="Barn with red roof and silos" style="left:404px;top:2361px;width:392px;height:274px;background:linear-gradient(180deg,#7e9fc6,#b31d1d 45%,#a38867 70%,#6b6a55)"></div>
  <div class="photo" role="img" aria-label="Blue shed with red framed door" style="left:808px;top:2361px;width:392px;height:274px;background:linear-gradient(135deg,#a9c8e6,#2e4a6b 45%,#c77a62 80%)"></div>
  <div class="photo" role="img" aria-label="Long red-roofed building with porch" style="left:404px;top:2648px;width:796px;height:273px;background:linear-gradient(180deg,#6fa0d8,#a7c3e0 40%,#c8232a 55%,#5b1a1a 75%,#8b8d8e)"></div>
  <div class="pill" style="left:524px;top:2998px;width:151px;height:51px">View More</div>
</section>

<section class="contact">
  <h2 class="heading section-title" style="top:90px">Contact Us</h2>
  <div class="rule" style="left:524px;top:159px;width:152px"></div>

  <div class="sub-title" style="left:112px;top:230px">Contact form</div>
  <div class="field" style="left:112px;top:297px;width:297px;height:33px">Name :</div>
  <div class="field" style="left:417px;top:297px;width:297px;height:33px">Phone no :</div>
  <div class="field" style="left:112px;top:343px;width:602px;height:33px">Email :</div>
  <div class="field" style="left:112px;top:389px;width:602px;height:79px">Message :</div>
  <div class="pill" style="left:606px;top:489px;width:108px;height:43px;font-size:13px">Submit</div>

  <div class="sub-title" style="left:778px;top:233px">Contact Information</div>
  <div class="info-icon" style="top:285px"><svg width="14" height="14" viewBox="0 0 24 24"><path fill="#e21b23" d="M6.6 10.8a15 15 0 0 0 6.6 6.6l2.2-2.2a1 1 0 0 1 1-.25 11.4 11.4 0 0 0 3.6.57 1 1 0 0 1 1 1V20a1 1 0 0 1-1 1A17 17 0 0 1 3 4a1 1 0 0 1 1-1h3.5a1 1 0 0 1 1 1c0 1.25.2 2.45.57 3.57a1 1 0 0 1-.25 1z"/></svg></div>
  <div class="info" style="left:836px;top:288px">555-012-0765</div>
  <div class="info-icon" style="top:341px"><svg width="14" height="14" viewBox="0 0 24 24" fill="#e21b23"><rect x="6" y="2" width="12" height="6"/><rect x="2" y="9" width="20" height="9" rx="2"/><rect x="6" y="15" width="12" height="7"/></svg></div>
  <div class="info" style="left:836px;top:344px">555-012-0994</div>
  <div class="info-icon" style="top:400px"><svg width="14" height="14" viewBox="0 0 24 24" fill="none" stroke="#e21b23" stroke-width="3"><circle cx="12" cy="12" r="9"/><path d="M12 7v5l3 2"/></svg></div>
  <div class="info" style="left:836px;top:403px">Monday - Friday: 7am - 5pm<br>Saturday: 7am - 12pm<br>Sunday: Closed</div>
</section>

<div class="footer-rule"></div>
<svg class="abs" style="left:1114px;top:3716px" width="28" height="18" viewBox="0 0 28 18"><path d="M2 16L14 4l12 12" fill="none" stroke="#aaa" stroke-width="3"/></svg>
<p class="copyright">Copyright © 2019, Dorvane Metal Inc. All rights reserved.</p>
<div class="social" style="left:949px"><i></i></div>
<div class="social" style="left:995px"><i></i></div>
<div class="social" style="left:1041px"><i></i></div>

</body>
</html>
```